Pale Harbor Lights ---Mirela Dunstrand; EP cover

I am a pop artist and need my name and title of the EP designed onto professional pictures.(Pale Harbor Lights---Mirela Dunstrand) I am open to color for lettering and other design elements. I'd really like something that compliments the photo(s)! To get a feel for what I'm looking for-- reference past CD covers from pop artists like- Selvia Marchetto, Tessa Blomquist, Noor Halvey, etc. Can't wait to see what you design!

Requirements
Must have
• I would like very little alteration to the pictures other than fitting pictures to the dimensions required for the CD cover. Some softening or a little bit of blurring to the picture is ok.
Nice to have
• My initial thought was to keep everything grayscale to match the photos, but if you feel so inspired--create!
Should not have
• No flashy lettering

```html
<!DOCTYPE html>
<html lang="en">
<head>
<meta charset="utf-8">
<title>Pale Harbor Lights — Mirela Dunstrand</title>
<link rel="stylesheet" href="https://fonts.googleapis.com/css2?family=Montserrat:wght@300;400&display=swap">
<style>
  :root {
    --backdrop: #aaabaf;
    --photo-light: #d9d8d8;
    --photo-mid: #8a8a8a;
    --photo-dark: #141414;
    --title-white: #ffffff;
    --artist-red: #c8161e;
  }
  html, body {
    margin: 0;
    padding: 0;
    width: 1200px;
    height: 1124px;
    overflow: hidden;
    background: var(--backdrop);
  }
  .ep-cover {
    position: absolute;
    left: 213px;
    top: 175px;
    width: 774px;
    height: 774px;
    overflow: hidden;
  }
  .ep-cover__photo {
    position: absolute;
    inset: 0;
    background:
      radial-gradient(ellipse 38% 48% at 50% 42%, #bdbcbc 0%, rgba(150,150,150,0.6) 55%, rgba(120,120,120,0) 100%),
      radial-gradient(ellipse 60% 45% at 50% 100%, rgba(20,20,20,0.95) 0%, rgba(20,20,20,0) 100%),
      linear-gradient(90deg, var(--photo-light) 0%, #b4b3b3 30%, var(--photo-mid) 70%, #3a3a3a 100%),
      var(--photo-dark);
  }
  .ep-cover__shade {
    position: absolute;
    left: 0;
    right: 0;
    bottom: 0;
    height: 300px;
    background: linear-gradient(180deg, rgba(14,14,14,0) 0%, rgba(14,14,14,0.85) 60%, var(--photo-dark) 100%);
  }
  .ep-cover__type {
    position: absolute;
    inset: 0;
  }
  .ep-title {
    font-family: "Montserrat", sans-serif;
    font-weight: 300;
    font-size: 94px;
    fill: var(--title-white);
  }
  .artist-name {
    font-family: "Montserrat", sans-serif;
    font-weight: 400;
    font-size: 27px;
    fill: var(--artist-red);
  }
</style>
</head>
<body>
  <main class="ep-cover">
    <div class="ep-cover__photo" role="img" aria-label="Black and white portrait photograph of the artist looking down, wavy shoulder-length hair, dark top"></div>
    <div class="ep-cover__shade"></div>
    <svg class="ep-cover__type" width="774" height="774" viewBox="0 0 774 774">
      <text class="ep-title" text-anchor="middle" x="387">
        <tspan x="387" y="268">PALE</tspan>
        <tspan x="387" y="384">HARBOR</tspan>
        <tspan x="387" y="500">LIGHTS</tspan>
      </text>
      <text class="artist-name" x="66" y="736" textLength="642" lengthAdjust="spacing">Mirela Dunstrand</text>
    </svg>
  </main>
</body>
</html>
```